I need a flyer that is professional, advertises and informs people about my health coaching practice. I am a Nationally Board Certified Health and Wellness Coach, lifestyle medicine certified and a lifestyle coach for the NHQ's Glucose Steady Initiative. I have my Master's Degree in Counseling Psychology. The final design should communicate evidence based health coaching that is self-directed and aimed at creating lasting health behavioral changes designed to enhance well-being. I am very open in terms of design but really would like a professional look to the flyer. I did want my contact information on the flyer: dana@vitalpathrecords.com and (217) 555-0148

Target Market(s)

Adults looking to improve their health, decrease risk factors for lifestyle disease, reduce weight, make better lifestyle choices to improve well-being.

Industry/Entity Type

Health And Wellness

Font styles to use
Sans Serif

Colors

Designer to choose colors to be used in the design.

Requirements
Must have
• Services offered, a professional feel, Dana Morrow Health Coaching (name of my practice), my phone number (217) 555-0148 and email: dana@vitalpathrecords.com, location: 1873 W Larkfield Avenue Bloomington IL 61709 my website: danamorrow.com to schedule appointments
Nice to have
• What is Health Coaching? Health and Wellness Coaches partner with clients seeking self-directed, lasting changes, aligned with their values, which promote health and wellness and, thereby, enhance well-being. In the course of their work health and wellness coaches display unconditional positive regard for their clients and a belief in their capacity for change, and honoring that each client is an expert on his or her life, while ensuring that all interactions are respectful and non-judgmental.

```html
<!DOCTYPE html>
<html lang="en">
<head>
<meta charset="utf-8">
<title>Dana Morrow Health Coaching – Flyer</title>
<link href="https://fonts.googleapis.com/css2?family=Roboto:wght@300;400;500;700&family=Roboto+Condensed:wght@400;700&display=swap" rel="stylesheet">
<style>
  :root{
    --stage:#1f4e78;
    --navy:#124a72;
    --teal:#1f8ea6;
    --teal-bright:#2599b0;
    --teal-text:#1b7f96;
    --gold:#c9962b;
    --gold-text:#c49a2c;
    --ink:#2b2b2b;
    --ink-soft:#444;
    --cream:#f6efe6;
    --white:#ffffff;
    --rule:#d9d9d9;
    --water-light:#d6eef2;
    --water:#7ccbd9;
  }
  *{box-sizing:border-box;margin:0;padding:0}
  html,body{width:1200px;height:1200px;overflow:hidden}
  body{background:var(--stage);font-family:"Roboto",sans-serif;position:relative}

  .page{position:absolute;overflow:hidden;box-shadow:0 6px 18px rgba(0,0,0,.35)}
  .abs{position:absolute}

  /* ---------- Front page ---------- */
  .front{left:28px;top:41px;width:574px;height:741px;background:linear-gradient(var(--white) 0,var(--white) 55%,var(--cream) 100%)}
  .front .brand-name{left:54px;top:26px;width:260px;text-align:center;color:var(--teal-text);font-size:31px;font-weight:400;letter-spacing:.5px;line-height:1.1}
  .front .brand-sub{left:54px;top:65px;width:260px;text-align:center;color:var(--teal-text);font-size:23px;font-weight:400}
  .front .brand-phone{left:363px;top:34px;color:var(--gold-text);font-size:19px}
  .hero-photo{left:0;top:100px;width:574px;height:320px;background:linear-gradient(180deg,var(--white) 0,var(--water-light) 30%,var(--water) 100%)}
  .hero-badge{left:298px;top:146px;width:248px;height:248px;border-radius:50%;background:var(--navy);color:var(--white);text-align:center;padding-top:58px}
  .hero-badge h2{font-weight:400;font-size:22.5px;line-height:28px}
  .hero-badge p{font-size:14px;line-height:18px;margin-top:16px}
  .front-wave{left:0;top:340px;width:574px;height:80px}
  .feature{width:132px;height:132px;border-radius:50%;border:4px solid var(--white);box-shadow:0 3px 8px rgba(0,0,0,.25)}
  .feature.food{left:58px;top:377px;background:#9a7f78}
  .feature.path{left:222px;top:372px;background:#6f7a55}
  .feature.tech{left:388px;top:373px;background:#b9d6e1}
  .intro-title{left:0;top:527px;width:574px;text-align:center;color:var(--teal-text);font-size:24px;font-weight:400}
  .intro-text{left:36px;top:569px;width:508px;font-family:"Roboto Condensed",sans-serif;font-size:9.8px;line-height:12.4px;color:var(--ink-soft)}
  .tagline{left:0;top:638px;width:574px;height:29px;background:var(--gold);color:#2b2414;text-align:center;font-size:14px;letter-spacing:3.6px;line-height:29px}
  .front-contact{left:0;top:667px;width:574px;height:74px;background:var(--teal);color:var(--white);text-align:center}
  .front-contact .line{font-size:14px;margin-top:10px}
  .front-contact .addr{font-size:17.5px;margin-top:7px}
  .sep{margin:0 9px}

  /* ---------- Services page ---------- */
  .services{left:614px;top:418px;width:564px;height:729px;background:linear-gradient(var(--white) 0,var(--white) 80%,var(--cream) 100%)}
  .services-head{left:0;top:0;width:564px;height:78px;background:var(--teal-bright);border-bottom:4px solid var(--gold);color:var(--white);text-align:center;font-size:29px;font-weight:300;line-height:76px;letter-spacing:.5px}
  .svc-title{left:41px;color:var(--teal-text);font-size:18px;font-weight:400;white-space:nowrap}
  .svc{left:41px;width:497px;display:flex;justify-content:space-between;font-family:"Roboto Condensed",sans-serif;font-size:11.3px;line-height:14.4px;color:var(--ink-soft)}
  .svc .info{width:410px}
  .svc .info b{color:var(--ink);font-weight:700;display:block}
  .svc .action{width:82px;text-align:center;position:relative}
  .svc .meta{color:var(--teal-text);font-weight:700;font-size:11.3px;white-space:nowrap}
  .book{display:block;margin:6px auto 0 5px;width:57px;height:20px;border-radius:4px;background:var(--teal-bright);color:var(--white);font-weight:700;font-size:11px;line-height:20px;text-align:center;letter-spacing:.5px}
  .rule{left:41px;width:512px;height:1px;background:var(--rule)}
  .footer-photo{left:0;top:500px;width:564px;height:150px;background:linear-gradient(180deg,rgba(255,255,255,0) 0,var(--water-light) 45%,var(--water) 100%)}
  .footer-wave{left:0;top:598px;width:564px;height:60px}
  .svc-brand{left:33px;top:552px;width:180px;text-align:center;color:var(--teal-text)}
  .svc-brand .n{font-size:21px;line-height:24px}
  .svc-brand .s{font-size:16.5px;margin-top:2px}
  .portrait{left:214px;top:529px;width:80px;height:80px;border-radius:50%;background:var(--gold);color:rgba(255,255,255,.35);font-size:17px;text-align:center;line-height:80px}
  .about{left:298px;top:512px;width:258px}
  .about h3{color:var(--teal-text);font-size:17px;font-weight:400;margin-bottom:5px}
  .about ul{list-style:none;font-family:"Roboto Condensed",sans-serif;font-size:9.7px;line-height:12.2px;color:var(--ink-soft)}
  .about li{position:relative;padding-left:14px}
  .about li svg{position:absolute;left:0;top:2px}
  .svc-contact{left:0;top:664px;width:564px;text-align:center}
  .svc-contact .line{color:var(--teal-text);font-size:14px}
  .svc-contact .addr{color:var(--gold-text);font-size:17px;margin-top:6px}
</style>
</head>
<body>

<section class="page front">
  <div class="abs brand-name">DANA MORROW</div>
  <div class="abs brand-sub">Health Coaching</div>
  <div class="abs brand-phone">(217) 555-0148</div>

  <div class="abs hero-photo" role="img" aria-label="Photo: white water lilies resting on turquoise water"></div>

  <div class="abs hero-badge">
    <h2>Health Coaching is<br>Embracing<br>Your Health</h2>
    <p>Let us help you build the<br>healthy life you deserve!</p>
  </div>

  <svg class="abs front-wave" viewBox="0 0 574 80" preserveAspectRatio="none" aria-hidden="true">
    <path d="M0 42 C120 70 260 40 380 30 C470 22 530 24 574 22 L574 80 L0 80Z" fill="var(--teal)"/>
    <path d="M0 40 C120 66 260 36 380 24 C470 14 530 12 574 10 L574 20 C520 22 460 22 380 30 C260 42 120 66 0 48Z" fill="var(--gold)"/>
    <path d="M0 52 C140 78 300 60 420 46 C490 40 540 40 574 40 L574 80 L0 80Z" fill="var(--white)"/>
    <path d="M0 44 C120 70 260 42 380 32 C470 25 530 26 574 26 L574 40 C540 40 490 40 420 46 C300 60 140 78 0 52Z" fill="var(--teal)"/>
  </svg>

  <div class="abs feature food" role="img" aria-label="Photo: heart-shaped bowl of fresh fruit and vegetables with a stethoscope"></div>
  <div class="abs feature path" role="img" aria-label="Photo: two people walking along a sunlit forest path"></div>
  <div class="abs feature tech" role="img" aria-label="Photo: hand touching glowing digital health icons"></div>

  <h2 class="abs intro-title">What is Health Coaching?</h2>
  <p class="abs intro-text">Health and Wellness Coaches partner with clients seeking self-directed, lasting changes, aligned with their values, which promote health and wellness and, thereby, enhance well-being. In the course of their work health and wellness coaches display unconditional positive regard for their clients and a belief in their capacity for change, and honoring that each client is an expert on his or her life, while ensuring that all interactions are respectful and non-judgmental.</p>

  <div class="abs tagline">Enhance your health. Enrich your life.</div>
  <div class="abs front-contact">
    <div class="line">(217) 555-0148<span class="sep">|</span>dana@vitalpathrecords.com<span class="sep">|</span>danamorrow.com</div>
    <div class="addr">1873 W Larkfield Avenue Bloomington IL 61709</div>
  </div>
</section>

<section class="page services">
  <div class="abs footer-photo" role="img" aria-label="Photo: white water lilies on turquoise water"></div>

  <h1 class="abs services-head">APPOINTMENT TYPES</h1>

  <h2 class="abs svc-title" style="top:98px">Health Coaching Initial Consultation</h2>
  <div class="abs svc" style="top:126px">
    <div class="info"><b>Health Coaching Data Collection</b>Evidence based health coaching is based in data. With the appropriate data, we can work together to reduce your risk for lifestyle disease the best wa…</div>
    <div class="action"><div class="meta" style="margin-top:4px">1 hr &nbsp;|&nbsp; $199</div><span class="book">BOOK</span></div>
  </div>
  <div class="abs rule" style="top:180px"></div>

  <div class="abs svc" style="top:187px">
    <div class="info"><b>Health Coaching Initial Consultation</b>Want to know if health coaching is right for you? I invite you to schedule an initial consultation with me. During this session, we will discuss your…</div>
    <div class="action"><div class="meta">30 min &nbsp;|&nbsp; Free</div><span class="book">BOOK</span></div>
  </div>
  <div class="abs rule" style="top:238px"></div>

  <h2 class="abs svc-title" style="top:247px">Health Coaching Individual 30 Minute Session</h2>
  <div class="abs svc" style="top:272px">
    <div class="info"><b>Individual Health Coaching 30 Minute Session</b>Partner with a Nationally Board Certified Health and Wellness Coach (NBC-HWC) for clients seeking self-directed, lasting changes, aligned with their v…</div>
    <div class="action"><div class="meta">30 min &nbsp;|&nbsp; $50</div><span class="book">BOOK</span></div>
  </div>
  <div class="abs rule" style="top:326px"></div>

  <h2 class="abs svc-title" style="top:332px">Health Coaching Package - Six 30 Minute Sessions</h2>
  <div class="abs svc" style="top:357px">
    <div class="info"><b>Individual Health Coaching 30 Minute Session</b>A focused health coaching session on the topics of your choice. Designed to get results, this package is shaped and molded around your goals and progr…</div>
    <div class="action"><div class="meta" style="margin-top:2px">30 min &nbsp;|&nbsp; $275</div><span class="book">BOOK</span></div>
  </div>
  <div class="abs rule" style="top:410px"></div>

  <h2 class="abs svc-title" style="top:417px">16 Week NHQ Diabetes Prevention Program - Steady Path</h2>
  <div class="abs svc" style="top:443px">
    <div class="info"><b>NHQ Steady Path Type 2 Diabetes Lifestyle 16 Week Program</b>Developed by the National Health Quarter (NHQ), a proven program to prevent or delay Type 2 Diabetes. Designed for people with prediabetes and also…</div>
    <div class="action"><div class="meta" style="margin-top:2px">1 hr &nbsp;|&nbsp; $249</div><span class="book">BOOK</span></div>
  </div>
  <div class="abs rule" style="top:502px"></div>

  <svg class="abs footer-wave" viewBox="0 0 564 60" preserveAspectRatio="none" aria-hidden="true">
    <path d="M0 40 C150 50 300 26 420 16 C490 10 540 8 564 8 L564 26 C520 26 470 28 420 32 C300 42 150 56 0 48Z" fill="var(--gold)"/>
    <path d="M0 48 C150 56 300 42 420 32 C470 28 520 26 564 26 L564 40 C520 40 470 40 420 42 C300 50 150 60 0 56Z" fill="var(--teal)"/>
    <path d="M0 56 C150 60 300 50 420 42 C470 40 520 40 564 40 L564 60 L0 60Z" fill="var(--white)"/>
  </svg>

  <div class="abs svc-brand"><div class="n">DANA MORROW</div><div class="s">Health Coaching</div></div>
  <div class="abs portrait" role="img" aria-label="Space for coach portrait photo">Photo</div>

  <div class="abs about">
    <h3>About Me</h3>
    <ul>
      <li><svg width="9" height="8" viewBox="0 0 9 8"><path d="M1 4 L3.5 6.5 L8 1" fill="none" stroke="var(--gold)" stroke-width="1.8"/></svg>Nationally Board Certified Health and Wellness Coach</li>
      <li><svg width="9" height="8" viewBox="0 0 9 8"><path d="M1 4 L3.5 6.5 L8 1" fill="none" stroke="var(--gold)" stroke-width="1.8"/></svg>lifestyle medicine certified and a lifestyle coach for the NHQ's Glucose Steady Initiative</li>
      <li><svg width="9" height="8" viewBox="0 0 9 8"><path d="M1 4 L3.5 6.5 L8 1" fill="none" stroke="var(--gold)" stroke-width="1.8"/></svg>Master's Degree in Counseling Psychology</li>
    </ul>
  </div>

  <div class="abs svc-contact">
    <div class="line">(217) 555-0148<span class="sep">|</span>dana@vitalpathrecords.com<span class="sep">|</span>danamorrow.com</div>
    <div class="addr">1873 W Larkfield Avenue Bloomington IL 61709</div>
  </div>
</section>

</body>
</html>
```